Hello my name is Colin, I am Starting a business called Harbor Health and fitness and am in need of a memorable business card.
It is a personal training studio. I have added the logo that i would like to be on the left center om my business card. i would like room left up the top for a heading sentence such as. "Is your body shocking for all the wrong reasons". there must be room left on the right of the logo below the main heading for 3 sub headings.
then under those 3 headings and logo room for another larger heading eg. "give me a call and learn how to eat chocolate, drink bear and have great sex". in what room is left i would like to be used for my contact details, use I'm Colin Pettersby your fitness expert on the left then on the right Phone, Email and website space in at least 12 Point. Very specific i know :) now onto the back, for the back i would like an eye catching graphic and room for one main headline and 3 bullet points centered just write anything i will choose what to put in them when i pick a winner. Thank you very much for sticking through all of that :) i appreciate you taking the time to read it and hopefully undergo designing me a business card.
I can't wait to see the designs!

Target Market(s)

slightly more towards females although it would probably be best if it was targeted towards both sexes

Industry/Entity Type

Training

Requirements
Nice to have
• I would love to see if anyone could come up with a design that would really make my card stand out and be memorable.
Should not have
• tacky fitness photos of abs and muscles etc.

```html
<!DOCTYPE html>
<html lang="en">
<head>
<meta charset="utf-8">
<title>Harbor Health and Fitness – Business Card Back</title>
<link rel="stylesheet" href="https://fonts.googleapis.com/css2?family=Questrial&family=Source+Sans+3:wght@400&display=swap">
<style>
  :root {
    --ink-deep: #0c0e0f;
    --ink-base: #2d3a40;
    --sweep-top: #3b4345;
    --sweep-bottom: #9fa9a8;
    --sliver-light: #d4d6d6;
    --sliver-dark: #5f6364;
    --band: #8fa09e;
    --disc: #f4f6f6;
    --disc-rim: #cfe3e1;
    --logo-ink: #3e4a4d;
    --text-light: #ffffff;
  }
  * { margin: 0; padding: 0; box-sizing: border-box; }
  html, body {
    width: 1200px;
    height: 720px;
    overflow: hidden;
    background: var(--ink-base);
  }
  .card {
    position: relative;
    width: 1200px;
    height: 720px;
    overflow: hidden;
  }
  .card-art {
    position: absolute;
    inset: 0;
    width: 1200px;
    height: 720px;
  }
  .main-headline {
    position: absolute;
    left: 128px;
    top: 74px;
    font-family: "Questrial", sans-serif;
    font-size: 39px;
    line-height: 50px;
    color: var(--text-light);
  }
  .sub-headings {
    position: absolute;
    left: 132px;
    top: 490px;
    list-style: none;
    font-family: "Source Sans 3", sans-serif;
    font-size: 37px;
    line-height: 48px;
    letter-spacing: 0.14em;
    color: var(--text-light);
  }
  .brand {
    position: absolute;
    left: 745px;
    top: 292px;
    width: 390px;
    font-family: "Questrial", sans-serif;
    color: var(--logo-ink);
    text-align: right;
  }
  .brand-name {
    display: block;
    font-size: 96px;
    line-height: 100px;
  }
  .brand-tagline {
    display: block;
    font-size: 27px;
    line-height: 32px;
    margin-top: 4px;
    padding-right: 12px;
  }
</style>
</head>
<body>
  <main class="card">
    <svg class="card-art" viewBox="0 0 1200 720" aria-hidden="true">
      <defs>
        <linearGradient id="ground" x1="0" y1="0" x2="0" y2="1">
          <stop offset="0" stop-color="var(--ink-deep)"/>
          <stop offset="1" stop-color="var(--ink-base)"/>
        </linearGradient>
        <linearGradient id="sweep" x1="0" y1="0" x2="0" y2="1">
          <stop offset="0" stop-color="var(--sweep-top)"/>
          <stop offset="0.75" stop-color="var(--sweep-bottom)"/>
        </linearGradient>
        <linearGradient id="sliver" x1="1" y1="0" x2="0" y2="1">
          <stop offset="0" stop-color="var(--sliver-light)"/>
          <stop offset="1" stop-color="var(--sliver-dark)"/>
        </linearGradient>
        <linearGradient id="band" x1="0" y1="0" x2="1" y2="0">
          <stop offset="0" stop-color="var(--band)" stop-opacity="0"/>
          <stop offset="0.45" stop-color="var(--band)" stop-opacity="0.55"/>
          <stop offset="1" stop-color="var(--band)"/>
        </linearGradient>
        <radialGradient id="disc" cx="0.5" cy="0.5" r="0.5">
          <stop offset="0.85" stop-color="var(--disc)"/>
          <stop offset="1" stop-color="var(--disc-rim)"/>
        </radialGradient>
      </defs>
      <rect class="ground" width="1200" height="720" fill="url(#ground)"/>
      <path class="sweep" fill="url(#sweep)"
        d="M0,496 C300,300 600,80 830,0 L1200,0 L1200,555 C1080,610 930,605 790,545 C620,470 430,425 260,438 C160,446 70,468 0,496 Z"/>
      <path class="sweep-sliver" fill="url(#sliver)"
        d="M0,496 C300,300 600,80 830,0 L1200,0 L1200,40 C900,30 600,160 0,496 Z" opacity="0.9"/>
      <rect class="headline-band" x="0" y="75" width="1200" height="48" fill="url(#band)"/>
      <circle class="brand-disc" cx="997" cy="363" r="208" fill="url(#disc)"/>
    </svg>

    <h1 class="main-headline">main headline</h1>

    <ul class="sub-headings">
      <li>1 sub heading</li>
      <li>2 sub heading</li>
      <li>3 sub heading</li>
    </ul>

    <div class="brand">
      <span class="brand-name">Harbor</span>
      <span class="brand-tagline">Health and Fitness</span>
    </div>
  </main>
</body>
</html>
```